Coffee House With Cycling Theme Wants Business Cards

We want to create a business card for a coffee house that has a cycling theme. We expect to use the current logo on one side of the business card and we have been considering adding the words 'COFFEE HOUSE' underneath (see example). For the other side of the business card we want an interesting design with tag-line, address and social media links (the normal business card stuff). See examples provided but we are not fixed on having it exactly as shown, we are very open to great creative ideas. Please note our logo has the initials ‘RV' in orange embedded in the design and this must be retained. However, you can play with the words COFFEE HOUSE as well as use the orange color on the backside of the business card, as you see fit. For an image on the backside of the business card it can be a photo, hand-drawn or whatever but it must visually combine coffee and cycling in some way. The interior of the Coffee House will be reclaimed wood, rustic and have an urban feel to it with cycling artifacts hanging from the walls/ceiling, etc. Finally, it would be beneficial if the business card design elements can be easily used on flyers and other promotional assets. Good luck, we are looking forward to seeing your creative ideas.

Target Market(s)

Coffee lovers and cycling fans

Contact Information for Business Card

See project description.

Colors

Designer to choose colors to be used in the design.

Requirements
Must have
• Must use the current logo provided and combine a coffee and bike theme.
Nice to have
• Orange is used in current logo and could be used as an accent color on the backside of the business card.

```html
<!DOCTYPE html>
<html lang="en">
<head>
<meta charset="utf-8">
<title>RV Coffee House – Business Card</title>
<link href="https://fonts.googleapis.com/css2?family=Open+Sans:wght@400;600&display=swap" rel="stylesheet">
<style>
  :root {
    --orange: #e8612a;
    --orange-deep: #c24f1f;
    --white: #ffffff;
    --paper-shade: #ececec;
    --ink: #2b2b2b;
    --arc: #3a3a3a;
    --light-grey: #cfcfcf;
    --stage: #3b3b3b;
  }
  * { margin: 0; padding: 0; box-sizing: border-box; }
  html, body { width: 1200px; height: 900px; overflow: hidden; }
  body {
    background: var(--stage);
    font-family: "Open Sans", sans-serif;
    position: relative;
  }
  .card {
    position: absolute;
    left: 285px;
    width: 630px;
    height: 360px;
    border-radius: 22px;
    overflow: hidden;
    box-shadow: 0 10px 30px rgba(0,0,0,.45);
  }
  .card--front { top: 70px; background: linear-gradient(160deg, var(--orange-deep), var(--orange) 70%); }
  .card--back  { top: 480px; background: linear-gradient(160deg, var(--orange), var(--orange-deep)); }

  .front-shape { position: absolute; inset: 0; }

  .contact {
    position: absolute;
    left: 40px;
    top: 78px;
    color: var(--white);
  }
  .contact__name { font-size: 24px; font-weight: 600; letter-spacing: 1.5px; text-transform: uppercase; }
  .contact__title { font-size: 15px; margin-bottom: 22px; }
  .contact__line { font-size: 15px; line-height: 1.55; display: flex; align-items: center; gap: 8px; }
  .contact__line svg { width: 12px; height: 12px; flex: none; }
  .contact__address { margin-bottom: 10px; }

  .brand {
    position: absolute;
    left: 390px;
    top: 120px;
    width: 220px;
    text-align: center;
  }
  .brand__name {
    font-size: 27px;
    font-weight: 600;
    color: var(--ink);
    letter-spacing: 1px;
    line-height: 1.15;
  }
  .social { margin-top: 22px; text-align: left; padding-left: 14px; }
  .social__item { display: flex; align-items: center; gap: 9px; font-size: 15px; color: var(--ink); margin-bottom: 6px; }
  .social__mark { width: 16px; height: 16px; background: var(--ink); flex: none; }
  .social__mark--round { border-radius: 50%; }

  .back-brand {
    position: absolute;
    inset: 0;
    display: flex;
    align-items: center;
    justify-content: center;
    font-size: 54px;
    font-weight: 400;
    letter-spacing: 3px;
    color: var(--light-grey);
    text-align: center;
    line-height: 1.1;
  }
</style>
</head>
<body>
  <section class="card card--front">
    <svg class="front-shape" viewBox="0 0 630 360" preserveAspectRatio="none" aria-hidden="true">
      <defs>
        <linearGradient id="paper" x1="0" y1="0" x2="1" y2="1">
          <stop offset="0" stop-color="#ffffff"/>
          <stop offset="1" stop-color="#e9e9e9"/>
        </linearGradient>
      </defs>
      <path d="M 395 0 Q 300 60 305 180 Q 315 300 430 360" fill="none" stroke="var(--arc)" stroke-width="9"/>
      <path d="M 410 0 Q 318 62 322 180 Q 332 300 450 360 L 630 360 L 630 0 Z" fill="url(#paper)"/>
    </svg>

    <div class="contact">
      <p class="contact__name">Daniel Harper</p>
      <p class="contact__title">Director</p>
      <p class="contact__line contact__address">42 Harlow Lane,<br>Riverton, NZ, 7040</p>
      <p class="contact__line">
        <svg viewBox="0 0 12 12"><path d="M3 1 L5 3 L4 4.5 Q5 7 7.5 8 L9 7 L11 9 L9.5 11 Q2 9.5 1 2.5 Z" fill="currentColor"/></svg>
        (555) 013-4821
      </p>
      <p class="contact__line">
        <svg viewBox="0 0 12 12"><rect x="1" y="2.5" width="10" height="7" fill="none" stroke="currentColor" stroke-width="1.2"/><path d="M1 2.5 L6 6.5 L11 2.5" fill="none" stroke="currentColor" stroke-width="1.2"/></svg>
        info@rvcoffeehouse.com
      </p>
      <p class="contact__line">
        <svg viewBox="0 0 12 12"><circle cx="6" cy="6" r="5" fill="none" stroke="currentColor" stroke-width="1.2"/><path d="M1 6 H11 M6 1 Q3 6 6 11 Q9 6 6 1" fill="none" stroke="currentColor" stroke-width="1"/></svg>
        www.rvcoffeehouse.com
      </p>
    </div>

    <div class="brand">
      <p class="brand__name">RV<br>COFFEE HOUSE</p>
      <div class="social">
        <p class="social__item"><span class="social__mark"></span>rvcoffeehouse.com</p>
        <p class="social__item"><span class="social__mark social__mark--round"></span>rvcoffeehouse.com</p>
      </div>
    </div>
  </section>

  <section class="card card--back">
    <p class="back-brand">RV<br>COFFEE HOUSE</p>
  </section>
</body>
</html>
```